Plastic Surgeon Stationery Design for a female surgeon

I would like a modern-classic stationery design ... I'm a 46 y.o plastic surgeon from Brasil and recently changed my life ( I was a navy surgeon for 18 years) . Now I'm on my office in Rio de Janeiro and I would like a classy design .
I have a fanpage with 76.000 followers on facebook and 12000 on instagram, and I love social media.
I like the colours like brown, beige ( something that I can use with the picture I'm attaching).

Target Market(s)

people who loves beauty, life

Industry/Entity Type

Plastic

Contact Information for Business Card

Dra Helena Moura de Castanheda e Lobo
Cirurgiã Plástica - Estética e Reconstrutiva
CRM 47.38592- 3 RQE 5813

Av. dos Coqueirais 3847 bl 03 cob 05
Vila do Sabiá - RJ - CEP 24587-000

Cons : (21) 2738-5169 Celular: (21) 97452-3361
helenamoura@caixapostal-exemplo.com

Logo Text

Helena de Castanheda - Cirurgiã Plástica

Font styles to use
Other font styles liked:
• I like the Scrip fonts but I'm open to sugestions

Colors
fbe7d2
ffffff
f8ba93
fee3d4
f9ba93
919191
757575
5c5c5c
9d9d9d

Requirements
Must have
• I would like my logo with something related to my initials and easy to use on merchandising stuff like pens, bags ...
Nice to have
• things related to happiness , graffic contents ( I love forms)
Should not have
• the plastic surgery cliches like female bodies , breasts , human parts ...

```html
<!DOCTYPE html>
<html lang="pt-BR">
<head>
<meta charset="utf-8">
<title>Helena de Castanheda – Cartão de visita</title>
<link rel="stylesheet" href="https://fonts.googleapis.com/css2?family=EB+Garamond:wght@400;700&display=swap">
<style>
  :root {
    --brown: #3e2b2d;
    --peach: #eab08a;
    --white: #ffffff;
    --ink: #2a1f20;
    --frame: #9d9d9d;
  }
  * { box-sizing: border-box; margin: 0; padding: 0; }
  html, body { width: 992px; height: 1200px; overflow: hidden; background: var(--white); }
  body { position: relative; font-family: "EB Garamond", Georgia, serif; color: var(--ink); }

  .card { position: absolute; left: 0; width: 992px; height: 560px; }
  .card--front { top: 0; height: 558px; background: var(--brown); }
  .card--back { top: 640px; background: var(--white); border: 1px solid var(--frame); }

  .brand { position: absolute; display: flex; align-items: center; }
  .brand__mark { border-radius: 50%; background: var(--peach); flex: none; }
  .brand__name {
    font-family: "EB Garamond", Georgia, serif;
    font-weight: 400;
    white-space: nowrap;
    line-height: 1;
  }

  .card--front .brand { left: 200px; top: 209px; }
  .card--front .brand__mark { width: 130px; height: 130px; margin-right: 30px; }
  .card--front .brand__name { color: var(--white); font-size: 46px; }

  .card--back .brand { left: 430px; top: 382px; }
  .card--back .brand__mark { width: 110px; height: 110px; margin-right: 26px; }
  .card--back .brand__name { color: var(--brown); font-size: 38px; }

  .accent-bar { position: absolute; left: -1px; top: -1px; width: 30px; height: 355px; background: var(--peach); }
  .accent-line { position: absolute; left: 29px; top: -1px; width: 6px; height: 355px; background: var(--brown); }

  .contact { position: absolute; left: 70px; top: 50px; font-size: 27px; line-height: 34px; }
  .contact__name { font-size: 32px; font-weight: 700; line-height: 40px; }
  .contact__address { margin-top: 30px; }
</style>
</head>
<body>
  <section class="card card--front">
    <div class="brand">
      <span class="brand__mark"></span>
      <span class="brand__name">Helena de Castanheda</span>
    </div>
  </section>

  <section class="card card--back">
    <span class="accent-bar"></span>
    <span class="accent-line"></span>
    <div class="contact">
      <p class="contact__name">Helena Moura de Castanheda e Lobo</p>
      <p>Cirurgiã Plástica - Estética e Reconstrutiva</p>
      <p>CRM 47.38592- 3 RQE 5813</p>
      <div class="contact__address">
        <p>Av. dos Coqueirais 3847 bl 03 cob 05</p>
        <p>Vila do Sabiá - RJ - CEP 24587-000</p>
        <p>Cons: (21) 2738-5169</p>
        <p>Celular: (21) 97452-3361</p>
        <p>helenamoura@caixapostal-exemplo.com</p>
      </div>
    </div>
    <div class="brand">
      <span class="brand__mark"></span>
      <span class="brand__name">Helena de Castanheda</span>
    </div>
  </section>
</body>
</html>
```